PostCard for Managed IT Services

We need a postcard design for a postcard that we intend to send out early in our marketing efforts to medical practices. The postcard should communicate our core services for small businesses including 1.) Managed IT Services, 2.) Security Services, 3.) Cloud Services, and 4.) IT Project and Integration work. company information is available at www.ferndaleit.com. I attached a two logos.WHILE WE WANT TO USE THE LOGO AND COLORS FROM OUR SITE, I HOPE THE DESIGN IS BOLD AND GRABS ATTENTION. I HOPE IT IS NOT THE 'SAME OLD' INFORMATION TECHNOLOGY LOOK. BE CREATIVE AND GET THE READER TO LOOK TWICE.

Target Market(s)

Businesses, medical practices

Font styles to use
Serif
Sans Serif

Requirements
Must have
• We need to include somewhere that are technicians are trained in on HIPAA and PCI (see site for info on the two)

```html
<!DOCTYPE html>
<html lang="en">
<head>
<meta charset="utf-8">
<title>Ferndale Managed Services – Postcard</title>
<link rel="stylesheet" href="https://fonts.googleapis.com/css2?family=Barlow+Semi+Condensed:wght@400;500&display=swap">
<style>
  :root {
    --stage: #d9dadc;
    --paper: #ffffff;
    --navy-deep: #1d1a4e;
    --navy: #2c2870;
    --navy-light: #3d3a8c;
    --band: #2a3fa8;
    --accent: #5d78c8;
    --icon-fill: #6f88d2;
    --ink-light: #ffffff;
    --rule: #222222;
  }
  * { box-sizing: border-box; margin: 0; padding: 0; }
  html, body { width: 1200px; height: 480px; overflow: hidden; }
  body {
    background: var(--stage);
    font-family: "Barlow Semi Condensed", "Arial Narrow", sans-serif;
    position: relative;
  }
  .card {
    position: absolute;
    top: 62px;
    width: 534px;
    height: 356px;
    background: var(--paper);
    overflow: hidden;
    box-shadow: 0 4px 10px rgba(0,0,0,0.25);
  }
  .card--front { left: 58px; }
  .card--back { left: 608px; }
  .card__art { position: absolute; inset: 0; width: 100%; height: 100%; }

  .headline {
    position: absolute; top: 28px; right: 40px;
    text-align: right; color: var(--ink-light); white-space: nowrap;
    font-size: 41px; font-weight: 500; line-height: 1;
  }
  .tagline {
    position: absolute; top: 83px; right: 40px; white-space: nowrap;
    color: var(--ink-light); font-size: 21px; font-weight: 400; line-height: 1;
  }
  .service { position: absolute; width: 112px; text-align: center; }
  .service__badge {
    width: 74px; height: 74px; margin: 0 auto;
    border-radius: 50%; background: var(--paper);
    display: flex; align-items: center; justify-content: center;
  }
  .service__badge svg { width: 46px; height: 46px; }
  .service__label {
    margin-top: 5px; color: var(--ink-light);
    font-size: 15px; font-weight: 500; line-height: 1.1; text-transform: uppercase;
  }
  .service--managed { left: 26px; top: 82px; }
  .service--security { left: 116px; top: 118px; }
  .service--cloud { left: 212px; top: 138px; }
  .service--project { left: 309px; top: 134px; }
  .service--integration { left: 402px; top: 127px; }

  .brand {
    position: absolute; display: flex; align-items: center; gap: 8px;
    font-size: 22px; font-weight: 500; line-height: 1;
  }
  .brand__dot { width: 14px; height: 14px; border-radius: 50%; flex: none; }
  .brand--front { left: 30px; top: 282px; color: var(--accent); }
  .brand--front .brand__dot { background: var(--accent); }
  .brand--back { left: 44px; top: 84px; color: var(--ink-light); }
  .brand--back .brand__dot { background: var(--ink-light); }

  .compliance {
    position: absolute; width: 150px; text-align: center;
    font-size: 10px; font-weight: 500; line-height: 1.35; letter-spacing: 0.12em;
  }
  .compliance--front { left: 18px; top: 318px; color: var(--accent); }
  .compliance--back { left: 36px; top: 132px; color: var(--ink-light); }

  .contact {
    position: absolute; display: flex; align-items: center; gap: 8px;
    color: var(--accent); font-size: 16.5px; font-weight: 400; line-height: 1.15;
  }
  .contact__icon {
    width: 28px; height: 28px; border-radius: 50%; background: var(--icon-fill);
    display: flex; align-items: center; justify-content: center; flex: none;
  }
  .contact__icon svg { width: 16px; height: 16px; }
  .contact--email { left: 179px; top: 282px; }
  .contact--phone { left: 376px; top: 282px; }
  .contact--address { left: 179px; top: 314px; }
  .contact--back-phone { left: 50px; top: 260px; font-size: 18px; }
  .contact--back-address { left: 50px; top: 296px; font-size: 18px; }
  .contact--back-phone .contact__icon,
  .contact--back-address .contact__icon { width: 32px; height: 32px; }

  .stamp-box {
    position: absolute; left: 442px; top: 39px; width: 68px; height: 68px;
    border: 1.5px solid var(--rule);
  }
  .address-line {
    position: absolute; left: 296px; width: 214px; height: 0;
    border-top: 1px solid var(--rule);
  }
  .address-line--1 { top: 230px; }
  .address-line--2 { top: 272px; }
  .address-line--3 { top: 315px; }
</style>
</head>
<body>

<section class="card card--front" aria-label="Postcard front">
  <svg class="card__art" viewBox="0 0 534 356" preserveAspectRatio="none">
    <defs>
      <linearGradient id="frontPhoto" x1="0" y1="0" x2="1" y2="1">
        <stop offset="0" stop-color="#4a3f7a"/>
        <stop offset="0.35" stop-color="var(--navy)"/>
        <stop offset="1" stop-color="var(--navy-deep)"/>
      </linearGradient>
    </defs>
    <rect width="534" height="356" fill="url(#frontPhoto)" role="img" aria-label="Photograph of a computer keyboard in deep blue light"/>
    <path d="M0,174 Q250,300 534,236 L534,356 L0,356 Z" fill="var(--paper)"/>
    <path d="M0,177 Q250,303 534,239" fill="none" stroke="var(--paper)" stroke-width="4"/>
    <path d="M0,180 Q250,306 534,242" fill="none" stroke="var(--band)" stroke-width="2"/>
    <path d="M0,188 Q250,315 534,250" fill="none" stroke="var(--band)" stroke-width="7"/>
  </svg>

  <h1 class="headline">Ferndale Managed Services</h1>
  <p class="tagline">Partner with the best for all your IT needs!</p>

  <div class="service service--managed">
    <div class="service__badge">
      <svg viewBox="0 0 42 42" fill="none" stroke="var(--accent)" stroke-width="2.4" stroke-linecap="round" stroke-linejoin="round">
        <path d="M9 10c-2 3 0 10 6 16s13 8 16 6l2-4-6-4-3 3c-3-1-7-5-8-8l3-3-4-6z"/>
        <text x="22" y="17" font-size="11" font-family="Barlow Semi Condensed, sans-serif" font-weight="500" fill="var(--accent)" stroke="none">24</text>
      </svg>
    </div>
    <p class="service__label">Managed IT<br>Services</p>
  </div>

  <div class="service service--security">
    <div class="service__badge">
      <svg viewBox="0 0 42 42" fill="none" stroke="var(--accent)" stroke-width="2.4" stroke-linejoin="round">
        <path d="M14 19v-5a7 7 0 0 1 14 0v5"/>
        <rect x="10" y="19" width="22" height="17" rx="2"/>
        <circle cx="21" cy="26" r="2.5"/>
        <path d="M21 28v4"/>
      </svg>
    </div>
    <p class="service__label">Security<br>Services</p>
  </div>

  <div class="service service--cloud">
    <div class="service__badge">
      <svg viewBox="0 0 42 42" fill="none" stroke="var(--accent)" stroke-width="2.2" stroke-linejoin="round">
        <path d="M12 30a7 7 0 0 1 0-14 9 9 0 0 1 17-2 7 7 0 0 1 2 14"/>
        <path d="M18 24v-3a3 3 0 0 1 6 0v3"/>
        <rect x="16" y="24" width="10" height="9" rx="1"/>
      </svg>
    </div>
    <p class="service__label">Cloud<br>Services</p>
  </div>

  <div class="service service--project">
    <div class="service__badge">
      <svg viewBox="0 0 42 42" fill="none" stroke="var(--accent)" stroke-width="2.2" stroke-linecap="round" stroke-linejoin="round">
        <path d="M15 27a9 9 0 1 1 12 0c-1 1-2 2-2 4h-8c0-2-1-3-2-4z"/>
        <path d="M17 35h8"/>
        <path d="M21 4v2M9 9l2 2M33 9l-2 2M5 19h2M35 19h2"/>
      </svg>
    </div>
    <p class="service__label">IT<br>Project</p>
  </div>

  <div class="service service--integration">
    <div class="service__badge">
      <svg viewBox="0 0 42 42" fill="none" stroke="var(--accent)" stroke-width="2.2" stroke-linecap="round">
        <rect x="14" y="8" width="14" height="26" rx="1.5"/>
        <path d="M8 13h6M8 19h6M8 25h6M8 31h6M28 13h6M28 19h6M28 25h6M28 31h6"/>
      </svg>
    </div>
    <p class="service__label">Integration<br>Work</p>
  </div>

  <div class="brand brand--front"><span class="brand__dot"></span>Ferndale IT</div>
  <p class="compliance compliance--front">Technicians trained in<br>HIPAA &amp; PCI compliance</p>

  <div class="contact contact--email">
    <span class="contact__icon">
      <svg viewBox="0 0 16 16" fill="none" stroke="#fff" stroke-width="1.4" stroke-linejoin="round"><rect x="2" y="4" width="12" height="9" rx="1"/><path d="M2 5l6 4 6-4"/></svg>
    </span>
    info@ferndaleit.com
  </div>
  <div class="contact contact--phone">
    <span class="contact__icon">
      <svg viewBox="0 0 16 16" fill="#fff"><path d="M3.5 2.5l2.5-.5 1.3 3-1.6 1.2c.7 1.6 1.9 2.8 3.5 3.5L10.4 8l3 1.3-.5 2.5c-5.3.6-10-4.1-9.4-9.3z"/></svg>
    </span>
    (555) 014-2287
  </div>
  <div class="contact contact--address">
    <span class="contact__icon">
      <svg viewBox="0 0 16 16" fill="none" stroke="#fff" stroke-width="1.4" stroke-linejoin="round"><path d="M8 14s-4.5-4.2-4.5-7.5a4.5 4.5 0 0 1 9 0C12.5 9.8 8 14 8 14z"/><circle cx="8" cy="6.5" r="1.6"/></svg>
    </span>
    2150 Harbor Rd, Suite 310, Lakeview, ND 58000
  </div>
</section>

<section class="card card--back" aria-label="Postcard back">
  <svg class="card__art" viewBox="0 0 534 356" preserveAspectRatio="none">
    <defs>
      <linearGradient id="backPhoto" x1="0" y1="0" x2="1" y2="1">
        <stop offset="0" stop-color="var(--navy-deep)"/>
        <stop offset="0.6" stop-color="var(--navy)"/>
        <stop offset="1" stop-color="var(--navy-light)"/>
      </linearGradient>
    </defs>
    <path d="M0,0 H368 Q190,190 0,246 Z" fill="url(#backPhoto)" role="img" aria-label="Photograph of a computer keyboard in deep blue light"/>
    <path d="M376,0 Q196,196 0,254" fill="none" stroke="var(--band)" stroke-width="2"/>
    <path d="M388,0 Q204,204 0,262" fill="none" stroke="var(--band)" stroke-width="7"/>
  </svg>

  <div class="brand brand--back"><span class="brand__dot"></span>Ferndale IT</div>
  <p class="compliance compliance--back">Technicians trained in<br>HIPAA &amp; PCI compliance</p>

  <div class="stamp-box" aria-label="Stamp area"></div>
  <div class="address-line address-line--1"></div>
  <div class="address-line address-line--2"></div>
  <div class="address-line address-line--3"></div>

  <div class="contact contact--back-phone">
    <span class="contact__icon">
      <svg viewBox="0 0 16 16" fill="#fff"><path d="M3.5 2.5l2.5-.5 1.3 3-1.6 1.2c.7 1.6 1.9 2.8 3.5 3.5L10.4 8l3 1.3-.5 2.5c-5.3.6-10-4.1-9.4-9.3z"/></svg>
    </span>
    (555) 014-2287
  </div>
  <div class="contact contact--back-address">
    <span class="contact__icon">
      <svg viewBox="0 0 16 16" fill="none" stroke="#fff" stroke-width="1.4" stroke-linejoin="round"><path d="M8 14s-4.5-4.2-4.5-7.5a4.5 4.5 0 0 1 9 0C12.5 9.8 8 14 8 14z"/><circle cx="8" cy="6.5" r="1.6"/></svg>
    </span>
    <span>2150 Harbor Rd, Suite 310,<br>Lakeview, ND 58000</span>
  </div>
</section>

</body>
</html>
```